Freeze Dried Raw Dog Food Label

Create a label for a Freeze Dried Raw dog and cat food line.
There are four flavors (beef, bison, fish and chicken).
4 x 8" Label FRONT AND BACK
Please see website www.morvelkitchen-example.com for our other product labels that this will need to stand next to.
Please use this color codes for the different flavors:
Chicken: #d5c55c
Beef: 469b9f
Bison: #275e6d
Fish: #a07980
The only other colors that should be used are Black, White, gray scale, and the shiny metallic gold as seen on our website: www.morvelkitchen-example.com
There will have 8 Variations:
Beef for dogs
Beef for Cats
Chicken for dogs
Chicken for cats
Bison for dogs
Bison for cats
Fish for dogs
Fish for cats.
There will be (2) 4X8 inch labels for each variation (a front side and a back side)
The Nutritional Information of the 4 flavors, is as follows:
BEEF
Ingredients
Beef, Beef Kidneys, Beef Hearts, Beef Liver, Whole Egg, Flaxseed, Organic Sweet Potato, Kelp, Organic Carrots, Organic Apples, Organic Blueberries, Cod Liver Oil, Pumpkin Seeds, Organic Spinach, Chicory Root, Organic Cranberries, Ginger, Mixed Tocopherols, Inulin, Dried Enterococcus faecium, Fermentation Product, Dried Lactobacillus acidophilus fermentation product
Calorie Content
Kcal/Cup 182
Guaranteed Analysis
Crude Protein – 38% (min)
Crude Fat – 36% (min)
Crude Fiber – 4% (max)
Moisture – 5% (max)
CHICKEN
Ingredients
Chicken, Chicken Liver, Chicken Hearts, Whole Egg, Flaxseed, Organic Sweet Potato, Kelp, Organic Carrots, Organic Apples, Organic Blueberries, Cod Liver Oil, Pumpkin Seeds, Organic Spinach, Chicory Root, Organic Cranberries, Ginger, Mixed Tocopherols, Inulin, Dried Enterococcus faecium, Fermentation Product, Dried Lactobacillus acidophilus fermentation product.
Calorie Content
Kcal/Cup 185
Guaranteed Analysis
Crude Protein – 45% (min)
Crude Fat – 34% (min)
Crude Fiber – 4% (max)
Moisture – 5% (max)
BISON:
Ingredients
Bison, Bison kidneys, Bison Livers, Whole Egg, Flaxseed, Organic Sweet Potato, Kelp, Organic Carrots, Organic Apples, Organic Blueberries, Cod Liver Oil, Pumpkin Seeds, Organic Spinach, Chicory Root, Organic Cranberries, Ginger, Mixed Tocopherols, Inulin, Dried Enterococcus faecium, Fermentation Product, Dried Lactobacillus acidophilus fermentation product.
Calorie Content
Kcal/Cup 186
Guaranteed Analysis
Crude Protein – 32% (min)
Crude Fat – 38% (min)
Crude Fiber – 5% (max)
Moisture – 5% (max)
FISH
Ingredients
Tuna, Salmon, Pollock, Whole Egg, Flaxseed, Organic Sweet Potato, Kelp, Organic Carrots, Organic Apples, Organic Blueberries, Cod Liver Oil, Pumpkin Seeds, Organic Spinach, Chicory Root, Organic Cranberries, Ginger, Mixed Tocopherols, Inulin, Dried Enterococcus faecium, Fermentation Product, Dried Lactobacillus acidophilus fermentation product.
Calorie Content
Kcal/Cup 455, Kcal/oz 114
Guaranteed Analysis
Crude Protein – 40% (min)
Crude Fat – 37% (min)
Crude Fiber – 4% (max)
Moisture – 5% (max)
THINGS TO ADD
Feeding Guidelines: Insert a QR CODE
Look and feel

```html
<!DOCTYPE html>
<html lang="en">
<head>
<meta charset="utf-8">
<title>Morvel Kitchen – Freeze-Dried Chicken Label Options</title>
<link rel="stylesheet" href="https://fonts.googleapis.com/css2?family=Oswald:wght@400;500;600;700&display=swap">
<style>
  :root{
    --chicken:#d5c55c;
    --black:#000000;
    --ink:#2b2b2b;
    --white:#ffffff;
    --paper:#f7f7f6;
    --stage-grey:#a7a9ac;
    --gold:linear-gradient(90deg,#8a5a12 0%,#c9962e 25%,#f6e7a1 50%,#c9962e 75%,#8a5a12 100%);
  }
  *{margin:0;padding:0;box-sizing:border-box;}
  html,body{width:1200px;height:716px;overflow:hidden;background:var(--white);}
  body{position:relative;font-family:"Oswald",sans-serif;}

  .backdrop{position:absolute;top:34px;height:635px;}
  .backdrop--one{left:53px;width:365px;background:var(--black);}
  .backdrop--two{left:418px;width:361px;background:var(--black);}
  .backdrop--three{left:779px;width:364px;background:var(--stage-grey);}

  .label{position:absolute;width:271px;height:540px;overflow:hidden;background:var(--paper);}
  .label--one{left:100px;top:72px;}
  .label--two{left:465px;top:81px;}
  .label--three{left:826px;top:81px;}

  .brand{position:absolute;left:0;width:100%;text-align:center;font-weight:700;
    font-size:22px;letter-spacing:2px;color:var(--black);line-height:1;}
  .brand__dot{display:inline-block;width:10px;height:10px;border-radius:50%;
    background:var(--black);margin-right:8px;vertical-align:middle;position:relative;top:-2px;}

  .lower{position:absolute;left:0;right:0;bottom:0;}
  .lower--chicken{top:233px;background:var(--chicken);}
  .lower--black{top:233px;background:var(--black);}

  .title-tab{position:absolute;left:19px;width:233px;top:0;height:263px;
    background:var(--paper);border-radius:0 0 8px 8px;}

  .gold-rule{position:absolute;left:50%;transform:translateX(-50%);width:60px;height:3px;background:var(--gold);}

  .kicker{position:absolute;left:0;width:100%;text-align:center;font-weight:500;
    font-size:21px;line-height:1;color:var(--ink);}
  .flavour{position:absolute;left:0;width:100%;text-align:center;font-weight:700;
    font-size:62px;line-height:1;letter-spacing:1px;color:var(--chicken);}

  .flavour-band{position:absolute;left:0;right:0;top:146px;height:130px;background:var(--chicken);}
  .flavour-band::before,.flavour-band::after{content:"";position:absolute;left:0;right:0;height:4px;background:var(--gold);}
  .flavour-band::before{top:0;}
  .flavour-band::after{bottom:0;}
  .flavour-band .kicker,.flavour-band .flavour{color:var(--white);}

  .edge-gold{position:absolute;left:0;right:0;height:6px;background:var(--gold);}
  .edge-gold--top{top:0;}
  .edge-gold--bottom{bottom:0;}

  .artwork{position:absolute;left:21px;width:228px;border-radius:4px;}
  .artwork--on-chicken{background:linear-gradient(180deg,rgba(255,255,255,.28),rgba(255,255,255,.12));}
  .artwork--on-paper{background:linear-gradient(180deg,#e4e4e4,#d2d2d2);}
  .artwork--on-black{background:linear-gradient(180deg,#5a4415,#2a200a);}

  .net-weight{position:absolute;left:0;width:100%;text-align:center;font-weight:500;font-size:10px;line-height:1;}
</style>
</head>
<body>

  <div class="backdrop backdrop--one"></div>
  <div class="backdrop backdrop--two"></div>
  <div class="backdrop backdrop--three"></div>

  <!-- Option one: chicken-coloured lower panel -->
  <section class="label label--one">
    <div class="lower lower--chicken"></div>
    <div class="title-tab"></div>
    <div class="brand" style="top:61px;"><span class="brand__dot"></span>MORVEL KITCHEN</div>
    <div class="gold-rule" style="top:141px;"></div>
    <div class="kicker" style="top:156px;">FREEZE-DRIED</div>
    <div class="flavour" style="top:180px;">CHICKEN</div>
    <div class="gold-rule" style="top:246px;"></div>
    <div class="artwork artwork--on-chicken" style="top:282px;height:232px;" role="img" aria-label="Line drawing of two sitting dogs in white outline"></div>
    <div class="net-weight" style="top:521px;color:var(--white);">NET WT. 4.4 LBS (2KG)</div>
  </section>

  <!-- Option two: white label with chicken band -->
  <section class="label label--two">
    <div class="brand" style="top:72px;"><span class="brand__dot"></span>MORVEL KITCHEN</div>
    <div class="flavour-band">
      <div class="kicker" style="top:18px;">FREEZE-DRIED</div>
      <div class="flavour" style="top:44px;">CHICKEN</div>
    </div>
    <div class="artwork artwork--on-paper" style="top:277px;height:220px;" role="img" aria-label="Line drawing of two sitting dogs in dark grey outline"></div>
    <div class="net-weight" style="top:520px;color:var(--ink);">NET WT. 4.4 LBS (2KG)</div>
  </section>

  <!-- Option three: black lower panel with gold edges -->
  <section class="label label--three">
    <div class="lower lower--black"></div>
    <div class="title-tab"></div>
    <div class="edge-gold edge-gold--top"></div>
    <div class="brand" style="top:72px;"><span class="brand__dot"></span>MORVEL KITCHEN</div>
    <div class="kicker" style="top:163px;">FREEZE-DRIED</div>
    <div class="flavour" style="top:186px;">CHICKEN</div>
    <div class="gold-rule" style="top:251px;"></div>
    <div class="artwork artwork--on-black" style="top:279px;height:227px;" role="img" aria-label="Line drawing of two sitting dogs in metallic gold outline"></div>
    <div class="net-weight" style="top:515px;color:var(--white);">NET WT. 4.4 LBS (2KG)</div>
    <div class="edge-gold edge-gold--bottom"></div>
  </section>

</body>
</html>
```